Wordpress Web Design For Midlifers.com

We're looking to update the design for www.midlifers.com. The website provides news and views for people aged 50 plus.

We want to use Wordpress as the content management tool and incorporate mailchimp to manage subscribers to our monthly newsletter.

In terms of design, we're looking for something simple and straightforward, we quite like the elder hub site, so something like that would be good. http://www.elderhub.org.uk
Updates

Project Deadline Extended
Reason: Dear All, Due to the Xmas break in the UK I've decided to extend the deadline by 7 days. Thanks for all your submissions, we will be making a decision shortly. Please note, as per the original brief, we are only interested in fully coded sites uploaded to our hosting provider. Please withdraw your design if you are not able to offer this complete solution. Thanks and good wishes to all!

Requirements
Must have
• Fully working wordpress templates that allow us to easily manage the website content. Easy for readers to use, navigate and read the content.
• Ideally a'turnkey' solution - the website built and ready for us to use wordpress to populate with content.

```html
<!DOCTYPE html>
<html lang="en">
<head>
<meta charset="utf-8">
<title>Midlifers.com – Travel</title>
<link rel="stylesheet" href="https://fonts.googleapis.com/css2?family=Open+Sans:wght@300;400;600&family=Arimo:wght@400&display=swap">
<style>
:root{
  --ink:#333;--muted:#8a8a8a;--soft:#a8a8a8;--line:#e3e3e3;
  --teal:#4fcfc2;--teal-dark:#2fb3a6;
  --orange-1:#ffad4a;--orange-2:#ff8a1e;
  --purple-1:#b65ee6;--purple-2:#9033cf;
  --green-1:#8dc63f;--green-2:#6aab20;--green-head:#79b52a;
  --pink:#f0609e;--footer:#2c2c2c;
  --n-home:#8cc63f;--n-travel:#4fcfc2;--n-health:#b8b28a;--n-hobbies:#f59a92;
  --n-lifestyle:#ee5a9c;--n-insurance:#6fa78f;--n-legal:#caa2ea;--n-comp:#f3b56c;--n-survey:#8cc63f;
}
*{box-sizing:border-box;margin:0;padding:0}
html,body{width:1200px;height:1200px;overflow:hidden;background:#fff}
body{font-family:"Open Sans",sans-serif;color:var(--ink)}
.stage{position:relative;width:1180px;height:1180px;transform:scale(1.01695);transform-origin:0 0;background:linear-gradient(#f8f8f8,#fff 260px)}
.abs{position:absolute}
.brand{left:82px;top:48px;display:flex;align-items:center;gap:10px;font-size:26px;font-weight:600;color:#5a9a1c}
.brand-dot{width:34px;height:34px;border-radius:50%;background:var(--green-1)}
.search{left:811px;top:74px;width:290px;height:28px;border:1px solid #d9d9d9;border-radius:14px;background:#fff;font-size:11px;font-style:italic;color:#999;padding:6px 14px}
.search svg{position:absolute;right:9px;top:6px}
.nav{left:78px;top:121px;width:1026px;height:49px;display:flex;border:1px solid var(--line);border-bottom:0;background:linear-gradient(#fff,#f1f1f1)}
.nav a{flex:1;text-align:center;font-size:16px;color:#444;text-decoration:none;line-height:46px;border-right:1px solid var(--line);border-bottom:4px solid}
.nav a:last-child{border-right:0}
.nav .active{background:var(--teal);color:#fff;font-weight:600}
.main{left:78px;top:169px;width:1026px;height:870px;border:1px solid var(--line);background:#fff}
.section-title{left:100px;top:198px;font-size:22px;color:#333}
.card{width:225px;height:252px;border:1px solid var(--line);background:#fff}
.card .photo{position:absolute;left:12px;top:10px;width:200px;height:92px}
.card h3{position:absolute;left:16px;top:112px;width:205px;font-weight:300;font-size:16.5px;line-height:21px;color:var(--muted)}
.card p{position:absolute;left:17px;top:157px;width:190px;font-size:11px;line-height:18px;color:var(--soft)}
.btn{position:absolute;left:18px;top:202px;width:96px;height:26px;background:linear-gradient(var(--teal),var(--teal-dark));color:#fff;font-size:12px;font-weight:600;text-align:center;line-height:26px;border-radius:2px}
.promo{left:801px;width:288px;border-radius:3px;color:#fff;padding:14px 20px}
.promo h2{font-weight:400;font-size:24px;line-height:30px}
.promo p{font-size:11px;line-height:15px;opacity:.85;margin-top:4px}
.register{top:181px;height:117px;background:linear-gradient(var(--orange-1),var(--orange-2))}
.register .cta{font-size:12px;font-weight:600;margin-top:8px}
.newsletter{top:305px;height:131px;background:linear-gradient(var(--purple-1),var(--purple-2));padding-left:24px}
.newsletter .field{position:relative;margin-top:7px;width:241px;height:27px;background:#fff;border-radius:3px}
.newsletter .field svg{position:absolute;right:8px;top:4px}
.donate{left:801px;top:443px;width:288px;height:213px;border:1px solid var(--line);background:#fff}
.donate .photo{width:286px;height:126px}
.donate h2{margin:6px 0 0 20px;font-weight:400;font-size:21px;color:var(--pink)}
.donate p{margin:4px 0 0 20px;font-size:11px;line-height:18px;color:var(--muted)}
.products{left:803px;top:667px;width:287px;height:327px;border-radius:3px;background:linear-gradient(var(--green-1),var(--green-2));color:#fff}
.products h2{height:49px;background:var(--green-head);font-weight:400;font-size:22px;padding:10px 26px}
.products ul{list-style:none;margin:8px 38px 0 30px}
.products li{display:flex;align-items:center;gap:7px;height:30px;font-size:13px;border-bottom:1px solid rgba(255,255,255,.25)}
.products li:last-child{border-bottom:0}
.footer{left:0;top:1049px;width:1180px;height:131px;background:var(--footer);color:#e8e8e8;font-family:"Arimo",sans-serif}
.footer .links{position:absolute;left:101px;font-size:14px;white-space:nowrap}
.footer .links span{margin:0 12px}
.footer .copy{position:absolute;left:100px;top:92px;font-size:11px}
</style>
</head>
<body>
<div class="stage">
  <div class="abs brand"><span class="brand-dot"></span>Midlifers.com</div>
  <div class="abs search">Search here..
    <svg width="16" height="16" viewBox="0 0 16 16"><circle cx="6.5" cy="6.5" r="5" fill="none" stroke="#666" stroke-width="1.6"/><line x1="10.2" y1="10.2" x2="14.5" y2="14.5" stroke="#666" stroke-width="1.8"/></svg>
  </div>
  <nav class="abs nav">
    <a style="border-bottom-color:var(--n-home)">Home</a>
    <a class="active" style="border-bottom-color:var(--n-travel)">Travel</a>
    <a style="border-bottom-color:var(--n-health)">Health</a>
    <a style="border-bottom-color:var(--n-hobbies)">Hobbies</a>
    <a style="border-bottom-color:var(--n-lifestyle)">Lifestyle</a>
    <a style="border-bottom-color:var(--n-insurance)">Insurance</a>
    <a style="border-bottom-color:var(--n-legal)">Legal</a>
    <a style="border-bottom-color:var(--n-comp)">Competitions</a>
    <a style="border-bottom-color:var(--n-survey)">Survey</a>
  </nav>
  <div class="abs main"></div>
  <div class="abs section-title">Featured Articles</div>

  <div class="abs card" style="left:95px;top:237px"><div class="photo" role="img" aria-label="Sunset over the sea with water bungalows" style="background:linear-gradient(#f2a15a,#e9c6a0 55%,#8a8fa0)"></div><h3>Cruise your way to a holiday bargain</h3><p>Cum sociis natoque penatibus et magnis dis parturient montes</p><span class="btn">READ MORE</span></div>
  <div class="abs card" style="left:328px;top:237px"><div class="photo" role="img" aria-label="Couple on a coastal hike with mountains behind" style="background:linear-gradient(#9cc6e8,#4d7fa3 60%,#b47d5c)"></div><h3>Avoid Winter Heating Costs with an Extended Stay</h3><p>Cum sociis natoque penatibus et magnis dis parturient montes</p><span class="btn">READ MORE</span></div>
  <div class="abs card" style="left:561px;top:237px"><div class="photo" role="img" aria-label="Hiker with backpack above a blue sea" style="background:linear-gradient(#2f7fcf,#6eb2e6 60%,#2a5d9a)"></div><h3>Westcountry Farm Pork Pie now Boarding the</h3><p>Cum sociis natoque penatibus et magnis dis parturient montes</p><span class="btn">READ MORE</span></div>

  <div class="abs card" style="left:95px;top:500px;height:251px"><div class="photo" role="img" aria-label="Couple relaxing in deck chairs on a beach" style="background:linear-gradient(#3aa6dc,#8fd3e8 55%,#2b5c8a)"></div><h3>Cruise your way to a holiday bargain</h3><p>Cum sociis natoque penatibus et magnis dis parturient montes</p><span class="btn">READ MORE</span></div>
  <div class="abs card" style="left:328px;top:500px;height:251px"><div class="photo" role="img" aria-label="Gondola on a Venetian canal" style="background:linear-gradient(#b9c3c8,#7f8a8c 55%,#4b5556)"></div><h3>Avoid Winter Heating Costs with an Extended Stay</h3><p>Cum sociis natoque penatibus et magnis dis parturient montes</p><span class="btn">READ MORE</span></div>
  <div class="abs card" style="left:561px;top:500px;height:251px"><div class="photo" role="img" aria-label="Tourists reading a map in an old town square" style="background:linear-gradient(#d9b99a,#c8a37f 55%,#8e6e56)"></div><h3>Westcountry Farm Pork Pie now Boarding the</h3><p>Cum sociis natoque penatibus et magnis dis parturient montes</p><span class="btn">READ MORE</span></div>

  <div class="abs card" style="left:95px;top:764px"><div class="photo" role="img" aria-label="Couple taking a photo in front of a historic building" style="background:linear-gradient(#c7c2bb,#8e8881 55%,#5e5a56)"></div><h3>Cruise your way to a holiday bargain</h3><p>Cum sociis natoque penatibus et magnis dis parturient montes</p><span class="btn">READ MORE</span></div>
  <div class="abs card" style="left:328px;top:764px"><div class="photo" role="img" aria-label="Couple walking through a city street" style="background:linear-gradient(#d2d6cf,#9da68f 55%,#6c7260)"></div><h3>Avoid Winter Heating Costs with an Extended Stay</h3><p>Cum sociis natoque penatibus et magnis dis parturient montes</p><span class="btn">READ MORE</span></div>
  <div class="abs card" style="left:561px;top:764px"><div class="photo" role="img" aria-label="Aeroplane silhouette against an orange sky" style="background:linear-gradient(#e58a2a,#f2a33a 55%,#c9651a)"></div><h3>Westcountry Farm Pork Pie now Boarding the</h3><p>Cum sociis natoque penatibus et magnis dis parturient montes</p><span class="btn">READ MORE</span></div>

  <div class="abs promo register">
    <h2>Register Now</h2>
    <p>Cum sociis natoque penatibus et magnis dis parturient montes, nascetur ridiculus mus</p>
    <div class="cta">CLICK HERE TO REGISTER NOW ›</div>
  </div>
  <div class="abs promo newsletter">
    <h2>Sign Up Newsletters</h2>
    <p>Cum sociis natoque penatibus et magnis dis parturient montes, nascetur ridiculus mus</p>
    <div class="field"><svg width="20" height="20" viewBox="0 0 20 20"><circle cx="10" cy="10" r="8.5" fill="none" stroke="#888" stroke-width="1.5"/><path d="M5 10h9M10.5 6l4 4-4 4" fill="none" stroke="#888" stroke-width="1.8"/></svg></div>
  </div>
  <div class="abs donate">
    <div class="photo" role="img" aria-label="Volunteers sorting clothing at a charity shop" style="background:linear-gradient(90deg,#6b4a3a,#b59a78 50%,#8e5b44)"></div>
    <h2>Donate today</h2>
    <p>Cum sociis natoque penatibus et magnis dis parturient montes, nascetur ridiculus mus</p>
  </div>
  <div class="abs products">
    <h2>Latest Products</h2>
    <ul>
      <li><svg width="14" height="14" viewBox="0 0 14 14"><circle cx="7" cy="7" r="7" fill="#fff"/><path d="M5.5 4l3 3-3 3" fill="none" stroke="#7ab82d" stroke-width="1.8"/></svg>Etiam est nunc</li>
      <li><svg width="14" height="14" viewBox="0 0 14 14"><circle cx="7" cy="7" r="7" fill="#fff"/><path d="M5.5 4l3 3-3 3" fill="none" stroke="#7ab82d" stroke-width="1.8"/></svg>Venenatis in tristique eu</li>
      <li><svg width="14" height="14" viewBox="0 0 14 14"><circle cx="7" cy="7" r="7" fill="#fff"/><path d="M5.5 4l3 3-3 3" fill="none" stroke="#7ab82d" stroke-width="1.8"/></svg>Imperdiet ac nisl</li>
      <li><svg width="14" height="14" viewBox="0 0 14 14"><circle cx="7" cy="7" r="7" fill="#fff"/><path d="M5.5 4l3 3-3 3" fill="none" stroke="#7ab82d" stroke-width="1.8"/></svg>Cum sociis natoque</li>
      <li><svg width="14" height="14" viewBox="0 0 14 14"><circle cx="7" cy="7" r="7" fill="#fff"/><path d="M5.5 4l3 3-3 3" fill="none" stroke="#7ab82d" stroke-width="1.8"/></svg>Penatibus et magnis</li>
      <li><svg width="14" height="14" viewBox="0 0 14 14"><circle cx="7" cy="7" r="7" fill="#fff"/><path d="M5.5 4l3 3-3 3" fill="none" stroke="#7ab82d" stroke-width="1.8"/></svg>Dis parturient montes</li>
      <li><svg width="14" height="14" viewBox="0 0 14 14"><circle cx="7" cy="7" r="7" fill="#fff"/><path d="M5.5 4l3 3-3 3" fill="none" stroke="#7ab82d" stroke-width="1.8"/></svg>Nascetur ridiculus mus</li>
      <li><svg width="14" height="14" viewBox="0 0 14 14"><circle cx="7" cy="7" r="7" fill="#fff"/><path d="M5.5 4l3 3-3 3" fill="none" stroke="#7ab82d" stroke-width="1.8"/></svg>Aculis facilisis massa</li>
    </ul>
  </div>

  <footer class="abs footer">
    <div class="links" style="top:32px">Home<span>|</span>Travel<span>|</span>Health<span>|</span>Hobbies<span>|</span>Lifestyle<span>|</span>Insurance<span>|</span>Legal<span>|</span>Competitions<span>|</span>Survey</div>
    <div class="links" style="top:61px">About Us<span>|</span>Advertise<span>|</span>Support<span>|</span>Blog<span>|</span>Contact</div>
    <div class="copy">Copyright © 2013 Midlifers. All Rights Reserved.</div>
  </footer>
</div>
</body>
</html>
```